Design some Business Cards

I need someone design a business card for me. My business is a retail for casual wears. Attachment is my brand and logo. Please integrate into the business card.

Business card must contain:

1: Slogan is Made for easy days
2: Contact info (address; email; Tel; website )

```html
<!DOCTYPE html>
<html lang="en">
<head>
<meta charset="utf-8">
<title>Oakmere Business Cards</title>
<link rel="stylesheet" href="https://fonts.googleapis.com/css2?family=Open+Sans:wght@400;600;700&display=swap">
<style>
  :root {
    --bg: #e8e5df;
    --card: #ffffff;
    --green-light: #74b043;
    --green-mid: #5a9233;
    --green-deep: #466f29;
    --green-dark: #3b5a22;
    --ink: #2f4a1c;
    --grey: #7a7a7a;
    --white: #ffffff;
  }
  * { box-sizing: border-box; margin: 0; padding: 0; }
  html, body {
    width: 1200px; height: 900px; overflow: hidden;
    background: var(--bg);
    font-family: "Open Sans", Arial, sans-serif;
  }
  .canvas { position: relative; width: 1200px; height: 900px; }

  .card {
    position: absolute;
    background: var(--card);
    border-radius: 24px;
    overflow: hidden;
    box-shadow: 0 6px 18px rgba(0,0,0,0.14);
  }

  /* Contact card (portrait) */
  .card-contact { left: 130px; top: 135px; width: 360px; height: 630px; }
  .card-contact .waves { position: absolute; inset: 0; }
  .identity { position: absolute; left: 38px; top: 72px; color: var(--ink); }
  .identity .name { font-size: 27px; font-weight: 400; letter-spacing: 0.5px; line-height: 1.1; }
  .identity .name strong { font-weight: 700; }
  .identity .role { font-size: 15px; letter-spacing: 2px; color: var(--ink); margin-top: 4px; }

  .contact-list { position: absolute; left: 30px; top: 330px; list-style: none; color: var(--white); }
  .contact-list li { display: flex; align-items: center; gap: 16px; height: 60px; font-size: 15px; letter-spacing: 0.5px; line-height: 1.35; }
  .contact-list .icon {
    width: 36px; height: 36px; flex: none;
    border: 2px solid var(--white); border-radius: 50%;
    display: flex; align-items: center; justify-content: center;
  }

  /* Brand card (landscape) */
  .card-brand { left: 550px; top: 285px; width: 600px; height: 343px; }
  .card-brand .corners { position: absolute; inset: 0; }
  .brand { position: absolute; left: 0; right: 0; top: 108px; text-align: center; }
  .brand-name {
    display: inline-flex; align-items: center; gap: 14px;
    font-size: 64px; font-weight: 400; color: var(--ink); letter-spacing: 1px; line-height: 1.2;
  }
  .brand-dot { width: 16px; height: 16px; border-radius: 50%; background: var(--ink); }
  .slogan { margin-top: 18px; font-size: 17px; letter-spacing: 6px; color: var(--grey); }
</style>
</head>
<body>
<main class="canvas">

  <section class="card card-contact">
    <svg class="waves" viewBox="0 0 360 630" preserveAspectRatio="none">
      <path d="M0,630 L0,300 Q150,150 360,130 L360,630 Z" fill="var(--green-light)"/>
      <path d="M0,630 L0,325 Q160,180 360,165 L360,630 Z" fill="var(--green-mid)"/>
      <path d="M0,630 L0,350 Q170,210 360,200 L360,630 Z" fill="var(--green-deep)"/>
      <path d="M0,630 L0,375 Q180,240 360,235 L360,630 Z" fill="var(--green-dark)"/>
    </svg>

    <div class="identity">
      <p class="name">MARLON <strong>HAYES</strong></p>
      <p class="role">GRAPHIC DESIGNER</p>
    </div>

    <ul class="contact-list">
      <li>
        <span class="icon">
          <svg width="18" height="14" viewBox="0 0 18 14"><rect x="1" y="1" width="16" height="12" rx="1.5" fill="none" stroke="#fff" stroke-width="1.8"/><path d="M1.5,2 L9,8 L16.5,2" fill="none" stroke="#fff" stroke-width="1.8"/></svg>
        </span>
        <span>HELLO@OAKMEREWEAR.COM</span>
      </li>
      <li>
        <span class="icon">
          <svg width="16" height="16" viewBox="0 0 16 16"><path d="M3,1 L6,1 L7,5 L5,6.5 Q6.5,9.5 9.5,11 L11,9 L15,10 L15,13 Q14,15 12,15 Q1,13 1,3 Q1,1 3,1 Z" fill="#fff"/></svg>
        </span>
        <span>+00 5550 2184 3307<br>+00 5550 9061 7725</span>
      </li>
      <li>
        <span class="icon">
          <svg width="14" height="18" viewBox="0 0 14 18"><path d="M7,17 Q1,9.5 1,6.5 A6,6 0 0 1 13,6.5 Q13,9.5 7,17 Z" fill="#fff"/><circle cx="7" cy="6.5" r="2.3" fill="var(--green-dark)"/></svg>
        </span>
        <span>BIRCH LANE 48<br>FERNVALE, USA.</span>
      </li>
      <li>
        <span class="icon">
          <svg width="18" height="18" viewBox="0 0 18 18"><circle cx="9" cy="9" r="7.5" fill="none" stroke="#fff" stroke-width="1.6"/><ellipse cx="9" cy="9" rx="3.2" ry="7.5" fill="none" stroke="#fff" stroke-width="1.4"/><path d="M1.5,9 H16.5" stroke="#fff" stroke-width="1.4"/></svg>
        </span>
        <span>WWW.OAKMEREWEAR.COM</span>
      </li>
    </ul>
  </section>

  <section class="card card-brand">
    <svg class="corners" viewBox="0 0 600 343" preserveAspectRatio="none">
      <path d="M500,0 Q570,30 600,115 L600,0 Z" fill="var(--green-light)"/>
      <path d="M530,0 Q582,32 600,90 L600,0 Z" fill="var(--green-mid)"/>
      <path d="M560,0 Q590,28 600,62 L600,0 Z" fill="var(--green-deep)"/>
      <path d="M500,343 Q570,313 600,228 L600,343 Z" fill="var(--green-light)"/>
      <path d="M530,343 Q582,311 600,253 L600,343 Z" fill="var(--green-mid)"/>
      <path d="M560,343 Q590,315 600,281 L600,343 Z" fill="var(--green-deep)"/>
    </svg>
    <div class="brand">
      <p class="brand-name"><span>Oakmere</span><span class="brand-dot"></span></p>
      <p class="slogan">Made for easy days</p>
    </div>
  </section>

</main>
</body>
</html>
```